Tall Ferns "Quiet Lane" New Single Cover

Create cover artwork for the band Tall Ferns' new single "Quiet Lane" being released early 2020. Style, font and graphics to be consistent with band's previous releases and overall brand identity. Visit www.tallfernsband.example and our Tunelane page https://music.example.net/artist/7KqPzTw2RxLmVbN4cYdJhE?si=GhTrWpLmZxQvBnKsYdFcRa to view our previous releases and overall brand identity. Some examples attached as well. We are looking for someone to work with on future projects as well.

Lyrics are here: https://files.example.org/document/d/4PxLm8TrQw2ZvKn7YbHcJdRfGsWe5AuNiOpXlMkBtCvE/edit

Music is here: https://audioshare.example.com/tallferns/quiet-lane/s-kdmwp

Font styles to use
Sans Serif

Colors

Designer to choose colors to be used in the design.

Requirements
Must have
• Must be consistent with current brand identity and with prior album / single art.

```html
<!DOCTYPE html>
<html lang="en">
<head>
<meta charset="utf-8">
<title>Tall Ferns – Quiet Lane</title>
<link rel="stylesheet" href="https://fonts.googleapis.com/css2?family=Josefin+Sans:wght@300;600&display=swap">
<style>
  :root {
    --pink-top: #ff98b1;
    --pink-mid: #f37f90;
    --pink-deep: #e9707f;
    --pink-base: #d97284;
    --navy: #1a2d5a;
    --white: #ffffff;
  }
  html, body {
    margin: 0;
    padding: 0;
    width: 1200px;
    height: 1200px;
    overflow: hidden;
  }
  .cover {
    position: relative;
    width: 1200px;
    height: 1200px;
    overflow: hidden;
    font-family: "Josefin Sans", sans-serif;
  }
  .cover-backdrop {
    position: absolute;
    inset: 0;
    background: linear-gradient(180deg,
      var(--pink-top) 0%,
      var(--pink-top) 12%,
      #f68a9c 28%,
      var(--pink-mid) 50%,
      var(--pink-deep) 70%,
      var(--pink-base) 85%,
      var(--pink-base) 100%);
  }
  .title-word {
    position: absolute;
    margin: 0;
    font-weight: 300;
    line-height: 1;
    color: var(--navy);
    text-transform: uppercase;
    letter-spacing: 0.02em;
  }
  .title-first {
    left: 104px;
    top: 116px;
    font-size: 382px;
  }
  .title-second {
    left: 104px;
    top: 414px;
    font-size: 382px;
  }
  .title-vertical {
    position: absolute;
    left: 836px;
    top: 130px;
    height: 920px;
    margin: 0;
    writing-mode: vertical-rl;
    font-weight: 300;
    font-size: 340px;
    line-height: 1;
    letter-spacing: 0.03em;
    color: var(--white);
    text-transform: uppercase;
  }
  .band-name {
    position: absolute;
    left: 106px;
    top: 950px;
    margin: 0;
    font-weight: 600;
    font-size: 66px;
    line-height: 1;
    letter-spacing: 0.12em;
    color: var(--navy);
    text-transform: uppercase;
  }
</style>
</head>
<body>
  <main class="cover">
    <div class="cover-backdrop" role="img" aria-label="Pink gradient backdrop with rows of soft triangular peaks, darkening toward the bottom"></div>
    <h1 class="title-word title-first">Qui</h1>
    <p class="title-word title-second">et</p>
    <p class="title-vertical">Lane</p>
    <p class="band-name">Tall Ferns</p>
  </main>
</body>
</html>
```